Business Card & Statioary Keystone Dwelling Survey Services
Keystone Dwelling Survey Services
Professional
Dennis Varga
President
2871 NE Juniper Ridge Ln.
Palm City, FL 34990
dvarga@keystonedwellingsurveyservices.com
www.keystonedwelingsurveyservices.com
FL State License DS8162
Along the long edge of the back of the card I would like a ruler. Also on the back I would like it to list under an INSPECTIONS heading, Pre-Sale, Pre-Purchase, 4-Point, Wind Mitigation.

```html
<!DOCTYPE html>
<html lang="en">
<head>
<meta charset="utf-8">
<title>Keystone Dwelling Survey Services – Stationery</title>
<link href="https://fonts.googleapis.com/css2?family=Cinzel:wght@700&family=Open+Sans:wght@400;600;700&display=swap" rel="stylesheet">
<style>
:root{
  --bg:#1c1d20;
  --paper:#ffffff;
  --blue:#1e5ea8;
  --blue-dark:#0f3566;
  --blue-light:#4f8fd3;
  --brown:#8a4a1c;
  --brown-dark:#4f2810;
  --orange:#e07a1f;
  --ink:#3a3a3a;
  --muted:#8a8f96;
}
*{margin:0;padding:0;box-sizing:border-box}
html,body{width:1200px;height:307px;overflow:hidden;background:var(--bg)}
body{position:relative;font-family:"Open Sans",Arial,sans-serif;color:var(--ink)}
.piece{position:absolute;overflow:hidden}
.brand{display:flex;align-items:center;gap:3px;font-family:"Cinzel",Georgia,serif;font-weight:700;color:var(--blue);line-height:1.05}
.brand-dot{flex:none;border-radius:50%;background:var(--orange)}
.brand-name{white-space:nowrap}
.wave{position:absolute;left:0;bottom:0;width:100%}
.watermark{position:absolute;border-radius:50%;background:var(--blue);opacity:.06}
/* master logo */
.master-logo{left:14px;top:18px;width:220px}
.master-logo .brand{font-size:11px;color:#e9eef5}
.master-logo .brand-dot{width:10px;height:10px}
.master-logo .tagline{margin-top:4px;font-size:7px;letter-spacing:1.5px;color:var(--orange);text-transform:uppercase}
.master-logo .sub{margin-top:2px;font-size:6px;color:var(--muted)}
/* business cards */
.card{width:110px;height:62px;border-radius:2px}
.card-front{background:var(--paper);padding:6px}
.card-front .brand{font-size:4.6px}
.card-front .brand-dot{width:5px;height:5px}
.card-front .person{position:absolute;left:6px;top:24px;font-size:4px;line-height:1.35}
.card-front .person strong{display:block;font-size:4.6px;color:var(--blue-dark)}
.card-front .contact{position:absolute;right:6px;top:22px;font-size:3.2px;line-height:1.4;text-align:right;color:var(--ink)}
.card-back{padding:6px 6px 6px 14px;color:#fff}
.card-back.blue{background:radial-gradient(circle at 70% 40%,var(--blue-light),var(--blue) 45%,var(--blue-dark))}
.card-back.brown{background:radial-gradient(circle at 70% 40%,#b5672d,var(--brown) 45%,var(--brown-dark))}
.card-back h3{font-size:5px;letter-spacing:1px;font-weight:700;margin-top:4px}
.card-back ul{list-style:none;font-size:4px;line-height:1.5;margin-top:2px}
.card-back .brand{font-size:4.2px;color:#fff;position:absolute;right:6px;bottom:6px}
.card-back .brand-dot{width:4px;height:4px}
.ruler{position:absolute;left:0;top:0;width:8px;height:100%;background:rgba(255,255,255,.18)}
/* letterhead */
.letterhead{width:208px;height:271px;top:12px;background:var(--paper);padding:12px}
.letterhead .brand{font-size:6.5px}
.letterhead .brand-dot{width:6px;height:6px}
.letterhead .contact{position:absolute;right:12px;top:12px;font-size:3.6px;line-height:1.5;text-align:right;color:var(--muted)}
.letterhead .watermark{width:110px;height:110px;left:49px;top:70px}
.letterhead .footer{position:absolute;left:0;right:0;bottom:6px;text-align:center;font-size:3.4px;color:#fff;z-index:2}
/* envelopes */
.envelope{width:204px;height:103px;background:var(--paper);padding:10px}
.envelope .brand{font-size:5.6px}
.envelope .brand-dot{width:5px;height:5px}
.envelope .address{font-size:3.4px;line-height:1.5;color:var(--muted);margin-top:3px;padding-left:8px}
.envelope .watermark{width:60px;height:60px;left:20px;top:30px}
.envelope.solid-blue{background:linear-gradient(160deg,var(--blue-light),var(--blue) 40%,var(--blue-dark))}
.envelope.solid-brown{background:linear-gradient(160deg,#b5672d,var(--brown) 40%,var(--brown-dark))}
.envelope.solid-blue .brand,.envelope.solid-brown .brand{color:#fff}
.envelope.plain{border:1px solid #d8dce2}
</style>
</head>
<body>

<section class="piece master-logo">
  <div class="brand"><span class="brand-dot"></span><span class="brand-name">Keystone Dwelling Survey Services</span></div>
  <div class="tagline">Professional</div>
  <div class="sub">Dennis Varga · President</div>
</section>

<!-- business cards -->
<article class="piece card card-front" style="left:12px;top:108px">
  <div class="brand"><span class="brand-dot"></span><span class="brand-name">Keystone Dwelling Survey Services</span></div>
  <div class="person"><strong>Dennis Varga</strong>President<br>FL State License DS8162</div>
  <div class="contact">2871 NE Juniper Ridge Ln.<br>Palm City, FL 34990<br>dvarga@keystonedwellingsurveyservices.com<br>www.keystonedwelingsurveyservices.com</div>
  <svg class="wave" viewBox="0 0 110 14" height="14" preserveAspectRatio="none"><path d="M0 8 Q40 0 110 6 L110 14 L0 14Z" fill="var(--blue)"/><path d="M0 11 Q50 4 110 9 L110 14 L0 14Z" fill="var(--blue-dark)"/></svg>
</article>

<article class="piece card card-back blue" style="left:125px;top:108px">
  <svg class="ruler" viewBox="0 0 8 62" preserveAspectRatio="none"><g stroke="#fff" stroke-width=".4"><path d="M0 4h5M0 8h3M0 12h5M0 16h3M0 20h5M0 24h3M0 28h5M0 32h3M0 36h5M0 40h3M0 44h5M0 48h3M0 52h5M0 56h3"/></g></svg>
  <h3>INSPECTIONS</h3>
  <ul><li>Pre-Sale</li><li>Pre-Purchase</li><li>4-Point</li><li>Wind Mitigation</li></ul>
  <div class="brand"><span class="brand-dot"></span><span class="brand-name">Keystone Dwelling Survey Services</span></div>
</article>

<article class="piece card card-front" style="left:12px;top:187px">
  <div class="brand"><span class="brand-dot"></span><span class="brand-name">Keystone Dwelling Survey Services</span></div>
  <div class="person"><strong>Dennis Varga</strong>President<br>FL State License DS8162</div>
  <div class="contact">2871 NE Juniper Ridge Ln.<br>Palm City, FL 34990<br>dvarga@keystonedwellingsurveyservices.com<br>www.keystonedwelingsurveyservices.com</div>
  <svg class="wave" viewBox="0 0 110 14" height="14" preserveAspectRatio="none"><path d="M0 8 Q40 0 110 6 L110 14 L0 14Z" fill="var(--brown)"/><path d="M0 11 Q50 4 110 9 L110 14 L0 14Z" fill="var(--brown-dark)"/></svg>
</article>

<article class="piece card card-back brown" style="left:125px;top:187px">
  <svg class="ruler" viewBox="0 0 8 62" preserveAspectRatio="none"><g stroke="#fff" stroke-width=".4"><path d="M0 4h5M0 8h3M0 12h5M0 16h3M0 20h5M0 24h3M0 28h5M0 32h3M0 36h5M0 40h3M0 44h5M0 48h3M0 52h5M0 56h3"/></g></svg>
  <h3>INSPECTIONS</h3>
  <ul><li>Pre-Sale</li><li>Pre-Purchase</li><li>4-Point</li><li>Wind Mitigation</li></ul>
  <div class="brand"><span class="brand-dot"></span><span class="brand-name">Keystone Dwelling Survey Services</span></div>
</article>

<!-- letterheads -->
<article class="piece letterhead" style="left:259px">
  <div class="brand"><span class="brand-dot"></span><span class="brand-name">Keystone Dwelling<br>Survey Services</span></div>
  <div class="contact">2871 NE Juniper Ridge Ln.<br>Palm City, FL 34990<br>dvarga@keystonedwellingsurveyservices.com<br>www.keystonedwelingsurveyservices.com</div>
  <div class="watermark"></div>
  <svg class="wave" viewBox="0 0 208 30" height="30" preserveAspectRatio="none"><path d="M0 14 Q80 0 208 10 L208 30 L0 30Z" fill="var(--blue-light)"/><path d="M0 19 Q100 6 208 16 L208 30 L0 30Z" fill="var(--blue)"/><path d="M0 24 Q110 14 208 22 L208 30 L0 30Z" fill="var(--blue-dark)"/></svg>
  <div class="footer">FL State License DS8162</div>
</article>

<article class="piece letterhead" style="left:492px">
  <div class="brand"><span class="brand-dot"></span><span class="brand-name">Keystone Dwelling<br>Survey Services</span></div>
  <div class="contact">2871 NE Juniper Ridge Ln.<br>Palm City, FL 34990<br>dvarga@keystonedwellingsurveyservices.com<br>www.keystonedwelingsurveyservices.com</div>
  <div class="watermark"></div>
  <svg class="wave" viewBox="0 0 208 30" height="30" preserveAspectRatio="none"><path d="M0 14 Q80 0 208 10 L208 30 L0 30Z" fill="var(--blue-light)"/><path d="M0 19 Q100 6 208 16 L208 30 L0 30Z" fill="var(--blue)"/><path d="M0 24 Q110 14 208 22 L208 30 L0 30Z" fill="var(--blue-dark)"/></svg>
  <div class="footer">FL State License DS8162</div>
</article>

<!-- envelopes -->
<article class="piece envelope" style="left:720px;top:12px">
  <div class="brand"><span class="brand-dot"></span><span class="brand-name">Keystone Dwelling Survey Services</span></div>
  <div class="address">2871 NE Juniper Ridge Ln.<br>Palm City, FL 34990</div>
  <div class="watermark"></div>
  <svg class="wave" viewBox="0 0 204 18" height="18" preserveAspectRatio="none"><path d="M0 9 Q80 0 204 6 L204 18 L0 18Z" fill="var(--blue)"/><path d="M0 13 Q100 5 204 11 L204 18 L0 18Z" fill="var(--blue-dark)"/></svg>
</article>

<article class="piece envelope" style="left:720px;top:168px">
  <div class="brand"><span class="brand-dot"></span><span class="brand-name">Keystone Dwelling Survey Services</span></div>
  <div class="address">2871 NE Juniper Ridge Ln.<br>Palm City, FL 34990</div>
  <div class="watermark"></div>
  <svg class="wave" viewBox="0 0 204 18" height="18" preserveAspectRatio="none"><path d="M0 9 Q80 0 204 6 L204 18 L0 18Z" fill="var(--brown)"/><path d="M0 13 Q100 5 204 11 L204 18 L0 18Z" fill="var(--brown-dark)"/></svg>
</article>

<article class="piece envelope solid-blue" style="left:972px;top:40px">
  <div class="brand"><span class="brand-dot"></span><span class="brand-name">Keystone Dwelling Survey Services</span></div>
</article>
<article class="piece envelope solid-brown" style="left:972px;top:100px">
  <div class="brand"><span class="brand-dot"></span><span class="brand-name">Keystone Dwelling Survey Services</span></div>
</article>
<article class="piece envelope plain" style="left:972px;top:160px">
  <div class="brand"><span class="brand-dot"></span><span class="brand-name">Keystone Dwelling Survey Services</span></div>
  <div class="address">2871 NE Juniper Ridge Ln.<br>Palm City, FL 34990</div>
</article>

</body>
</html>
```